Lumo Sound Bourse Design - platform for listeners to invest in the artists they love

We need a preview of a couple pages of what our app might look like to put on our website before launch. It is a Music streaming platform and NFT marketplace where users can invest in artists and own music royalties. there needs to be a user profile and portfolio showing returns for their collections. the NFT exchange should have artists and NFT listings with album art, the home page can be similar to tunevale we need pages for mobile and desktop version.

For inspiration look at;
tunevale
gemdock
mintora

should be similar to a tunevale and mintora mashup

some images are attached for ideas

Target Market(s)

Crypto native musicians/listeners

Industry/Entity Type

Music streaming/ NFT

Font styles to use
Other font styles liked:
• Arial

Requirements
Must have
• Must have a place to buy/sell NFTs listen to music/ check portfolio performance and collection
Nice to have
• a percent gain and loss on the NFTs someone owns would be nice smooth easy to use design

```html
<!DOCTYPE html>
<html lang="en">
<head>
<meta charset="utf-8">
<title>Lumo Sound – Collections &amp; Portfolio Performance</title>
<link href="https://fonts.googleapis.com/css2?family=Poppins:wght@400;500;600;700&display=swap" rel="stylesheet">
<style>
:root{
  --page:#0b0e24;
  --app:#141722;
  --side:#1a1d29;
  --card:#1c2030;
  --card-2:#232839;
  --line:#2c3246;
  --blue:#3d6bf7;
  --text:#ffffff;
  --muted:#b9bdcc;
  --dim:#8a90a3;
}
*{box-sizing:border-box;margin:0;padding:0}
html,body{width:1200px;height:2310px;overflow:hidden;background:var(--page)}
body{position:relative;font-family:"Poppins",Arial,sans-serif;color:var(--text)}
.abs{position:absolute}
svg{display:block}

/* headers */
.hero{left:0;top:0;width:1200px;height:229px;background:linear-gradient(180deg,#0b0f2e 0%,#111a4a 100%)}
.hero-waves{left:0;top:0;width:1200px;height:229px;background:radial-gradient(ellipse 260px 90px at 80px 70px,rgba(40,140,220,.55),transparent 70%),radial-gradient(ellipse 300px 110px at 1130px 80px,rgba(50,150,230,.5),transparent 70%),radial-gradient(ellipse 500px 90px at 600px 220px,rgba(40,60,190,.45),transparent 75%)}
.hero-note{left:0;width:1200px;top:56px;text-align:center;font-size:22px;letter-spacing:1.5px;font-weight:500}
.section-title{left:0;width:1200px;text-align:center;font-size:46px;font-weight:600;letter-spacing:.5px;white-space:nowrap}

/* desktop */
.desktop{left:0;top:229px;width:1200px;height:854px;background:var(--app);overflow:hidden}
.sidebar{left:0;top:0;width:216px;height:777px;background:var(--side)}
.brand{left:37px;top:29px;font-size:18px;font-weight:600;color:var(--blue)}
.nav-head{left:35px;font-size:14px;color:#e4e6ee}
.nav-item{left:35px;display:flex;align-items:center;gap:18px;font-size:14px;color:#e4e6ee}
.nav-item svg{width:15px;height:15px}
.nav-item.active{font-weight:600;color:#fff}
.active-bar{left:212px;top:356px;width:4px;height:38px;background:var(--blue)}

.search{border:1.5px solid #d8dbe5;border-radius:22px;display:flex;align-items:center;gap:10px;padding-left:15px;color:#e8eaf1;white-space:nowrap}
.btn-primary{background:var(--blue);border-radius:22px;display:flex;align-items:center;justify-content:center;font-weight:500;box-shadow:0 6px 18px rgba(61,107,247,.35);white-space:nowrap}

.panel{background:var(--card);border-radius:18px}
.artwork-storm{background:radial-gradient(circle at 70% 40%,#9fb6e8 0%,#4c6cb8 20%,#1d3272 55%,#0c173f 100%);border-radius:14px}
.handle{color:#d9dcea}
.name{font-weight:600}
.joined{color:#c7cbda}
.wallet{background:#11141f;border-radius:8px;display:flex;align-items:center;gap:7px;color:#e4e6ee;white-space:nowrap}
.wallet .dot{width:7px;height:7px;border-radius:50%;background:#fff}
.follow{border:1.5px solid #fff;border-radius:16px;display:flex;align-items:center;justify-content:center;font-weight:600}
.share{background:#fff;border-radius:6px;display:flex;align-items:center;justify-content:center}

.perf-title{font-weight:600}
.perf-pct{color:var(--blue);font-weight:600;display:flex;align-items:center;gap:6px}
.axis{fill:#c9ccd8;font-family:"Poppins",Arial,sans-serif}

.tab{border-radius:6px;background:var(--card);display:flex;align-items:center;justify-content:center;color:#d8dbe6;white-space:nowrap}
.tab.on{background:var(--blue);color:#fff;font-weight:600}

.nft{background:var(--card);border-radius:16px;overflow:hidden}
.nft-art{position:absolute;border-radius:4px}
.avatar{position:absolute;border-radius:50%;border:2px solid rgba(255,255,255,.6);background:radial-gradient(circle at 50% 40%,#f1efe9,#8c8a86 70%)}
.chip{position:absolute;font-size:10px;color:#fff;background:rgba(0,0,0,.45);border-radius:3px;padding:1px 6px;white-space:nowrap}
.nft-title{position:absolute;font-size:12px;font-weight:600;white-space:nowrap}
.nft-artist{position:absolute;font-size:12px;color:#d3d6e2;white-space:nowrap}
.nft-offer{position:absolute;font-size:10px;color:#d3d6e2;text-align:right}
.nft-price{position:absolute;font-size:11px;color:var(--blue);font-weight:600;text-align:right}

.player{background:var(--card-2)}
.progress{height:3px;background:#e8eaf1}
.progress i{display:block;height:3px;background:var(--blue)}
.thumb-aurora{background:linear-gradient(160deg,#27314a 0%,#3f8f6a 45%,#a6d98a 60%,#202838 100%);border-radius:4px}
.track{font-weight:500;white-space:nowrap}
.track small{display:block;color:#c8cbd8;font-weight:400}
.play{background:var(--blue);border-radius:7px;display:flex;align-items:center;justify-content:center}

/* mobile */
.mobile-bg{left:0;top:1083px;width:1200px;height:1227px;background:radial-gradient(ellipse 900px 700px at 900px 1100px,#2a1a78 0%,transparent 70%),linear-gradient(180deg,#1c1650 0%,#0a0920 40%,#14123c 100%)}
.phone{left:377px;top:1289px;width:447px;height:966px;background:var(--app);overflow:hidden}
.mob-nav{left:0;top:871px;width:447px;height:95px;background:var(--side)}
</style>
</head>
<body>

<!-- Desktop heading -->
<div class="abs hero"></div>
<div class="abs hero-waves" role="img" aria-label="Flowing blue light ribbons"></div>
<p class="abs hero-note">Please scroll through bottom. Thanks</p>
<h1 class="abs section-title" style="top:158px">Collections &amp; Portfolio Performance - Desktop</h1>

<!-- Desktop screen -->
<section class="abs desktop">
  <aside class="abs sidebar">
    <div class="abs brand">Lumo Sound</div>
    <div class="abs nav-head" style="top:103px">HOMEPAGE</div>
    <div class="abs nav-item" style="top:136px">
      <svg viewBox="0 0 16 16"><circle cx="8" cy="8" r="7" fill="#fff"/><path d="M10.8 5.2 9 9 5.2 10.8 7 7z" fill="#1a1d29"/></svg>Explore</div>
    <div class="abs nav-item" style="top:175px">
      <svg viewBox="0 0 16 16" fill="#fff"><ellipse cx="8" cy="3.5" rx="5" ry="2"/><path d="M3 5.5c0 1.1 2.2 2 5 2s5-.9 5-2v2.5c0 1.1-2.2 2-5 2s-5-.9-5-2zM3 10c0 1.1 2.2 2 5 2s5-.9 5-2v2.5c0 1.1-2.2 2-5 2s-5-.9-5-2z"/></svg>Auction</div>
    <div class="abs nav-item" style="top:213px">
      <svg viewBox="0 0 16 16" fill="#fff"><rect x="1" y="3" width="10" height="1.6"/><rect x="1" y="7" width="10" height="1.6"/><rect x="1" y="11" width="6" height="1.6"/><circle cx="11" cy="12" r="2"/><rect x="12.3" y="5" width="1.5" height="7"/></svg>Playlist</div>
    <div class="abs nav-head" style="top:256px">NFT</div>
    <div class="abs nav-item" style="top:289px">
      <svg viewBox="0 0 16 16" fill="#fff"><path d="M5 3 14 1v10.5a2.2 2 0 1 1-1.5-1.9V4.5L6.5 5.8v7.7A2.2 2 0 1 1 5 11.6z"/></svg>Collections</div>
    <div class="abs nav-item" style="top:327px">
      <svg viewBox="0 0 16 16" fill="#fff"><path d="M1 14V11l3-3 3 2 4-5 4 2v7z"/></svg>Portfolio</div>
    <div class="abs nav-item active" style="top:365px">
      <svg viewBox="0 0 16 16" fill="#fff"><circle cx="8" cy="4.5" r="3.5"/><path d="M1.5 15c0-3.6 2.9-6 6.5-6s6.5 2.4 6.5 6z"/></svg>Account</div>
  </aside>
  <div class="abs active-bar"></div>

  <div class="abs search" style="left:247px;top:31px;width:661px;height:40px;font-size:12px">
    <svg width="17" height="17" viewBox="0 0 18 18" fill="none" stroke="#fff" stroke-width="1.6"><circle cx="8" cy="8" r="6"/><path d="m12.5 12.5 4 4"/></svg>
    Search music, collection, and artist here...
  </div>
  <div class="abs btn-primary" style="left:1006px;top:31px;width:167px;height:40px;font-size:14px">Connect Wallet</div>

  <!-- profile -->
  <div class="abs panel" style="left:247px;top:113px;width:541px;height:197px">
    <div class="abs artwork-storm" style="left:25px;top:25px;width:147px;height:147px" role="img" aria-label="Profile artwork: lightning in a blue stormy sky"></div>
    <div class="abs handle" style="left:194px;top:36px;font-size:14px">@ToTheMoon</div>
    <div class="abs name" style="left:194px;top:55px;font-size:18px">To The Moon</div>
    <div class="abs joined" style="left:194px;top:89px;font-size:12px">Joined, January 2022</div>
    <div class="abs wallet" style="left:194px;top:139px;width:178px;height:22px;padding-left:10px;font-size:11px"><span class="dot"></span>0x4c1be27a9f03d8aa....71e</div>
    <div class="abs share" style="left:406px;top:39px;width:27px;height:27px">
      <svg width="15" height="15" viewBox="0 0 16 16" fill="#1c2030"><circle cx="12" cy="3.5" r="2.3"/><circle cx="4" cy="8" r="2.3"/><circle cx="12" cy="12.5" r="2.3"/><path d="M4 8 12 3.5M4 8l8 4.5" stroke="#1c2030" stroke-width="1.5"/></svg>
    </div>
    <div class="abs follow" style="left:454px;top:39px;width:64px;height:27px;font-size:12px">Follow</div>
  </div>

  <!-- portfolio -->
  <div class="abs panel" style="left:810px;top:113px;width:363px;height:197px">
    <div class="abs perf-title" style="left:24px;top:27px;font-size:17px">Portfolio Performance</div>
    <div class="abs perf-pct" style="left:277px;top:27px;font-size:16px">91.57%<svg width="10" height="6" viewBox="0 0 10 6"><path d="M0 6 5 0l5 6z" fill="#3d6bf7"/></svg></div>
    <svg class="abs" style="left:0;top:60px" width="363" height="137" viewBox="0 0 363 137">
      <line x1="24" y1="21" x2="291" y2="21" stroke="#c9ccd8" stroke-dasharray="4 5"/>
      <line x1="291" y1="4" x2="291" y2="110" stroke="#c9ccd8" stroke-dasharray="3 4"/>
      <path d="M24 109V100L30 90 38 95 45 92 55 75 68 48 78 58 88 55 98 60 110 56 122 60 132 45 142 30 152 22 160 12 166 3 172 10 180 30 188 42 196 50 204 46 212 55 220 50 230 47 238 58 246 60 254 52 262 55 270 65 278 80 286 95 290 109Z" fill="#3d6bf7"/>
      <g class="axis" font-size="10" text-anchor="end">
        <text x="348" y="25">9,400.00</text><text x="348" y="52">9,300.00</text><text x="348" y="79">9,200.00</text><text x="348" y="107">9,100.00</text>
      </g>
      <g class="axis" font-size="10" text-anchor="middle">
        <text x="38" y="123">JAN</text><text x="91" y="123">FEB</text><text x="148" y="123">MAR</text><text x="201" y="123">APR</text><text x="257" y="123">MAY</text>
      </g>
    </svg>
  </div>

  <!-- tabs -->
  <div class="abs tab on" style="left:247px;top:346px;width:123px;height:38px;font-size:13px">Collected (12)</div>
  <div class="abs tab" style="left:382px;top:346px;width:122px;height:38px;font-size:13px">Created (0)</div>
  <div class="abs tab" style="left:514px;top:346px;width:122px;height:38px;font-size:13px">Favorited (0)</div>
  <div class="abs tab" style="left:645px;top:346px;width:123px;height:38px;font-size:13px">Playlist (1)</div>

  <!-- NFT cards row 1 -->
  <div class="abs nft" style="left:247px;top:405px;width:213px;height:254px">
    <div class="nft-art" style="left:13px;top:15px;width:184px;height:175px;background:linear-gradient(180deg,#3a1e2a 0%,#7a2a2c 35%,#c9523a 55%,#2a3a4a 80%,#141c28 100%)" role="img" aria-label="Album art: neon-lit night street with a car in the rain"></div>
    <div class="avatar" style="left:19px;top:21px;width:28px;height:28px" role="img" aria-label="Collector avatar"></div>
    <span class="chip" style="left:18px;top:172px">3:49</span><span class="chip" style="left:160px;top:172px">EDM</span>
    <div class="nft-title" style="left:13px;top:205px">Till It Fades ft. Ra..</div>
    <div class="nft-artist" style="left:13px;top:225px">Velvet Harbor</div>
    <div class="nft-offer" style="right:16px;top:206px">Best Offer</div>
    <div class="nft-price" style="right:16px;top:229px">27.04 ETH</div>
  </div>
  <div class="abs nft" style="left:484px;top:405px;width:214px;height:254px">
    <div class="nft-art" style="left:13px;top:15px;width:184px;height:175px;background:radial-gradient(circle at 45% 50%,#a9bfe2 0%,#3c5f9c 25%,#183467 60%,#0d1d45 100%)" role="img" aria-label="Album art: cloud in a starry blue night sky"></div>
    <div class="avatar" style="left:19px;top:21px;width:28px;height:28px" role="img" aria-label="Collector avatar"></div>
    <span class="chip" style="left:18px;top:172px">4:18</span><span class="chip" style="left:94px;top:172px">Progressive House</span>
    <div class="nft-title" style="left:13px;top:205px">The Night</div>
    <div class="nft-artist" style="left:13px;top:225px">Aveline</div>
    <div class="nft-offer" style="right:16px;top:206px">Best Offer</div>
    <div class="nft-price" style="right:16px;top:229px">2.5 ETH</div>
  </div>
  <div class="abs nft" style="left:722px;top:405px;width:213px;height:254px">
    <div class="nft-art" style="left:13px;top:15px;width:184px;height:175px;background:linear-gradient(180deg,#9cc3ee 0%,#cfe0f2 40%,#b44a46 60%,#8c8d8e 75%,#5d5e60 100%)" role="img" aria-label="Album art: lighthouse under a blue sky"></div>
    <div class="avatar" style="left:19px;top:21px;width:28px;height:28px" role="img" aria-label="Collector avatar"></div>
    <span class="chip" style="left:18px;top:172px">5:41</span><span class="chip" style="left:162px;top:172px">Pop</span>
    <div class="nft-title" style="left:13px;top:205px">Mend the Sky</div>
    <div class="nft-artist" style="left:13px;top:225px">Marlo Jensen</div>
    <div class="nft-offer" style="right:16px;top:206px">Best Offer</div>
    <div class="nft-price" style="right:16px;top:229px">5.54 ETH</div>
  </div>
  <div class="abs nft" style="left:960px;top:405px;width:213px;height:254px">
    <div class="nft-art" style="left:13px;top:15px;width:184px;height:175px;background:linear-gradient(160deg,#5c8fa8 0%,#c9b3b0 45%,#eab9a6 75%,#d99e90 100%)" role="img" aria-label="Album art: pastel pink clouds in a blue sky"></div>
    <div class="avatar" style="left:19px;top:21px;width:28px;height:28px" role="img" aria-label="Collector avatar"></div>
    <span class="chip" style="left:18px;top:172px">2:31</span><span class="chip" style="left:160px;top:172px">EDM</span>
    <div class="nft-title" style="left:13px;top:205px">Paradise</div>
    <div class="nft-artist" style="left:13px;top:225px">Dara Quillon</div>
    <div class="nft-offer" style="right:16px;top:206px">Best Offer</div>
    <div class="nft-price" style="right:16px;top:229px">12 ETH</div>
  </div>

  <!-- NFT cards row 2 (cut by player) -->
  <div class="abs nft" style="left:247px;top:680px;width:213px;height:200px">
    <div class="nft-art" style="left:13px;top:15px;width:184px;height:175px;background:linear-gradient(180deg,#5a6aa0 0%,#c98a8a 60%,#2a2230 100%)" role="img" aria-label="Album art: tree silhouette at sunset"></div>
    <div class="avatar" style="left:19px;top:21px;width:28px;height:28px" role="img" aria-label="Collector avatar"></div>
  </div>
  <div class="abs nft" style="left:484px;top:680px;width:214px;height:200px">
    <div class="nft-art" style="left:13px;top:15px;width:184px;height:175px;background:linear-gradient(180deg,#8fd0d6 0%,#5fa8b4 70%,#2d4a58 100%)" role="img" aria-label="Album art: mountain peak above teal water"></div>
    <div class="avatar" style="left:19px;top:21px;width:28px;height:28px" role="img" aria-label="Collector avatar"></div>
  </div>
  <div class="abs nft" style="left:722px;top:680px;width:213px;height:200px">
    <div class="nft-art" style="left:13px;top:15px;width:184px;height:175px;background:linear-gradient(170deg,#e07a68 0%,#c3574c 50%,#4f6c86 100%)" role="img" aria-label="Album art: coral red clouds"></div>
    <div class="avatar" style="left:19px;top:21px;width:28px;height:28px" role="img" aria-label="Collector avatar"></div>
  </div>
  <div class="abs nft" style="left:960px;top:680px;width:213px;height:200px">
    <div class="nft-art" style="left:13px;top:15px;width:184px;height:175px;background:linear-gradient(170deg,#1f2a2c 0%,#3e4a4c 50%,#121818 100%)" role="img" aria-label="Album art: dark smoke clouds"></div>
    <div class="avatar" style="left:19px;top:21px;width:28px;height:28px" role="img" aria-label="Collector avatar"></div>
  </div>

  <!-- player -->
  <div class="abs player" style="left:0;top:777px;width:1200px;height:77px">
    <div class="abs progress" style="left:0;top:0;width:1200px"><i style="width:921px"></i></div>
    <div class="abs thumb-aurora" style="left:36px;top:20px;width:40px;height:40px" role="img" aria-label="Cover art: green aurora over a lake"></div>
    <div class="abs track" style="left:90px;top:18px;font-size:17px;line-height:1.25">Rise Up Slow<small style="font-size:12px">Aveline</small></div>
    <svg class="abs" style="left:477px;top:32px" width="18" height="18" viewBox="0 0 18 18" fill="none" stroke="#fff" stroke-width="1.6"><path d="M3 8V6h11l-3-3M15 10v2H4l3 3"/></svg>
    <svg class="abs" style="left:534px;top:35px" width="12" height="12" viewBox="0 0 12 12" fill="#fff"><rect x="0" y="0" width="2" height="12"/><path d="M12 0v12L3 6z"/></svg>
    <div class="abs play" style="left:583px;top:24px;width:34px;height:34px"><svg width="14" height="14" viewBox="0 0 14 14"><path d="M2 0v14l12-7z" fill="#fff"/></svg></div>
    <svg class="abs" style="left:653px;top:35px" width="12" height="12" viewBox="0 0 12 12" fill="#fff"><rect x="10" y="0" width="2" height="12"/><path d="M0 0v12l9-6z"/></svg>
    <svg class="abs" style="left:704px;top:32px" width="18" height="18" viewBox="0 0 18 18" fill="none" stroke="#fff" stroke-width="1.6"><path d="M1 4h3l9 10h3M1 14h3l9-10h3M14 2l2 2-2 2M14 12l2 2-2 2"/></svg>
    <div class="abs" style="left:857px;top:30px;font-size:13px;white-space:nowrap">3:26 <span style="color:#fff">/</span> <span style="color:#c8cbd8">4:33</span></div>
    <svg class="abs" style="left:942px;top:31px" width="20" height="18" viewBox="0 0 20 18" fill="none" stroke="#fff" stroke-width="1.6"><path d="M2 6h4l5-4v14l-5-4H2z"/><path d="M14 6c1.5 1.6 1.5 4.4 0 6M16.5 3.5c3 3 3 8 0 11"/></svg>
    <div class="abs" style="left:975px;top:39px;width:155px;height:2px;background:#fff"></div>
    <div class="abs" style="left:975px;top:39px;width:49px;height:2px;background:var(--blue)"></div>
    <div class="abs" style="left:1018px;top:34px;width:12px;height:12px;border-radius:50%;background:#fff;border:3px solid var(--blue)"></div>
    <svg class="abs" style="left:1157px;top:33px" width="15" height="13" viewBox="0 0 15 13" fill="#fff"><rect x="4" y="0" width="11" height="1.6"/><rect x="4" y="5.5" width="11" height="1.6"/><rect x="4" y="11" width="11" height="1.6"/><rect x="0" y="0" width="2" height="1.6"/><rect x="0" y="5.5" width="2" height="1.6"/><rect x="0" y="11" width="2" height="1.6"/></svg>
  </div>
</section>

<!-- Mobile heading -->
<div class="abs mobile-bg"></div>
<h2 class="abs section-title" style="top:1178px">Collections &amp; Portfolio Performance - Mobile</h2>

<!-- Mobile screen -->
<section class="abs phone">
  <div class="abs search" style="left:16px;top:20px;width:257px;height:38px;font-size:14px;padding-left:13px">
    <svg width="20" height="20" viewBox="0 0 18 18" fill="none" stroke="#fff" stroke-width="1.4"><circle cx="8" cy="8" r="6.5"/><path d="m12.8 12.8 4 4"/></svg>
    Search music, collection...
  </div>
  <div class="abs btn-primary" style="left:289px;top:20px;width:143px;height:38px;font-size:14.5px">Connect Wallet</div>

  <div class="abs panel" style="left:16px;top:97px;width:415px;height:143px;border-radius:12px">
    <div class="abs artwork-storm" style="left:9px;top:11px;width:121px;height:121px;border-radius:12px" role="img" aria-label="Profile artwork: lightning in a blue stormy sky"></div>
    <div class="abs handle" style="left:144px;top:12px;font-size:15px">@ToTheMoon</div>
    <div class="abs name" style="left:144px;top:37px;font-size:19px">To The Moon</div>
    <div class="abs joined" style="left:144px;top:69px;font-size:12.5px">Joined, January 2022</div>
    <div class="abs wallet" style="left:138px;top:98px;width:253px;height:34px;padding-left:14px;font-size:15px;border-radius:10px"><span class="dot" style="width:9px;height:9px"></span>0x4c1be27a9f03d8aa....71e</div>
    <div class="abs follow" style="left:300px;top:13px;width:91px;height:37px;font-size:16px;border-radius:20px;border-width:2px">Follow</div>
  </div>

  <div class="abs panel" style="left:16px;top:260px;width:415px;height:223px;border-radius:12px">
    <div class="abs perf-title" style="left:18px;top:10px;font-size:17px">Portfolio Performance</div>
    <div class="abs perf-pct" style="left:317px;top:10px;font-size:16px">91.57%<svg width="14" height="8" viewBox="0 0 14 8"><path d="M0 8 7 0l7 8z" fill="#3d6bf7"/></svg></div>
    <svg class="abs" style="left:0;top:0" width="415" height="223" viewBox="0 0 415 223">
      <line x1="10" y1="89" x2="330" y2="89" stroke="#c9ccd8" stroke-dasharray="5 7"/>
      <line x1="331" y1="60" x2="331" y2="187" stroke="#c9ccd8" stroke-dasharray="3 4"/>
      <path d="M10 187V168L20 173 30 178 40 170 50 172 60 160 72 130 84 118 96 128 106 120 116 130 128 126 140 130 150 122 160 110 172 105 182 96 191 75 198 90 208 110 218 122 228 118 238 128 248 126 258 140 268 132 280 134 290 130 300 135 310 142 318 150 325 165 329 187Z" fill="#3d6bf7"/>
      <g class="axis" font-size="14" text-anchor="end">
        <text x="390" y="68">9,400.00</text><text x="390" y="107">9,300.00</text><text x="390" y="146">9,200.00</text><text x="390" y="185">9,100.00</text>
      </g>
      <g class="axis" font-size="13" text-anchor="middle">
        <text x="30" y="207">JAN</text><text x="106" y="207">FEB</text><text x="187" y="207">MAR</text><text x="262" y="207">APR</text>
      </g>
    </svg>
  </div>

  <div class="abs tab on" style="left:26px;top:521px;width:176px;height:54px;font-size:19px;border-radius:8px">Collected (12)</div>
  <div class="abs tab" style="left:219px;top:521px;width:176px;height:54px;font-size:19px;border-radius:8px">Created (0)</div>
  <div class="abs tab" style="left:408px;top:521px;width:176px;height:54px;font-size:19px;border-radius:8px;justify-content:flex-start;padding-left:32px">Favorited (0)</div>

  <div class="abs nft" style="left:26px;top:597px;width:305px;height:330px;border-radius:24px">
    <div class="nft-art" style="left:19px;top:21px;width:265px;height:260px;background:linear-gradient(180deg,#3a1e2a 0%,#7a2a2c 35%,#c9523a 55%,#2a3a4a 80%,#141c28 100%)" role="img" aria-label="Album art: neon-lit night street with a car in the rain"></div>
    <div class="avatar" style="left:28px;top:30px;width:56px;height:56px" role="img" aria-label="Collector avatar"></div>
  </div>
  <div class="abs nft" style="left:367px;top:597px;width:305px;height:330px;border-radius:24px">
    <div class="nft-art" style="left:19px;top:21px;width:265px;height:260px;background:radial-gradient(circle at 45% 50%,#a9bfe2 0%,#3c5f9c 25%,#183467 60%,#0d1d45 100%)" role="img" aria-label="Album art: cloud in a starry blue night sky"></div>
    <div class="avatar" style="left:28px;top:30px;width:56px;height:56px" role="img" aria-label="Collector avatar"></div>
  </div>

  <div class="abs player" style="left:0;top:811px;width:447px;height:60px">
    <div class="abs progress" style="left:0;top:0;width:447px"><i style="width:238px"></i></div>
    <div class="abs thumb-aurora" style="left:16px;top:9px;width:48px;height:48px" role="img" aria-label="Cover art: green aurora over a lake"></div>
    <div class="abs track" style="left:78px;top:11px;font-size:15px;line-height:1.35;font-weight:600">Rise Up Slow<small style="font-size:15px">Aveline</small></div>
    <svg class="abs" style="left:313px;top:25px" width="15" height="15" viewBox="0 0 12 12" fill="#fff"><rect x="0" y="0" width="2" height="12"/><path d="M12 0v12L3 6z"/></svg>
    <div class="abs play" style="left:349px;top:14px;width:38px;height:38px;border-radius:50%"><svg width="14" height="14" viewBox="0 0 14 14"><path d="M2 0v14l12-7z" fill="#fff"/></svg></div>
    <svg class="abs" style="left:409px;top:25px" width="15" height="15" viewBox="0 0 12 12" fill="#fff"><rect x="10" y="0" width="2" height="12"/><path d="M0 0v12l9-6z"/></svg>
  </div>

  <nav class="abs mob-nav">
    <svg class="abs" style="left:42px;top:38px" width="20" height="20" viewBox="0 0 16 16"><circle cx="8" cy="8" r="7.5" fill="#3d6bf7"/><path d="M11 5 9.2 9.2 5 11l1.8-4.2z" fill="#1a1d29"/></svg>
    <svg class="abs" style="left:156px;top:40px" width="20" height="18" viewBox="0 0 16 16" fill="#fff"><rect x="1" y="3" width="10" height="1.6"/><rect x="1" y="7" width="10" height="1.6"/><rect x="1" y="11" width="6" height="1.6"/><circle cx="11" cy="12" r="2"/><rect x="12.3" y="5" width="1.5" height="7"/></svg>
    <svg class="abs" style="left:271px;top:37px" width="20" height="21" viewBox="0 0 16 16" fill="#fff"><path d="M5 3 14 1v10.5a2.2 2 0 1 1-1.5-1.9V4.5L6.5 5.8v7.7A2.2 2 0 1 1 5 11.6z"/></svg>
    <svg class="abs" style="left:385px;top:37px" width="20" height="21" viewBox="0 0 16 16" fill="#fff"><circle cx="8" cy="4.5" r="3.5"/><path d="M1.5 15c0-3.6 2.9-6 6.5-6s6.5 2.4 6.5 6z"/></svg>
  </nav>
</section>

</body>
</html>
```